Brava Nest (Smart Home, Installation, Repair Industry) (Contest)

Looking for a website design for my company
Services we offer:
Phone Repair
TV Mounting
Security Camera Installation
Networking / Wi-Fi
Smart Home Services
IT Support

Looking for a website similar to trovely.example

Few tabs
About Us
Contact Us
Areas Served
Pricing and Services

```html
<!DOCTYPE html>
<html lang="en">
<head>
<meta charset="utf-8">
<title>Brava Nest — Smart Home, Installation, Repair</title>
<link href="https://fonts.googleapis.com/css2?family=Rubik:wght@400;500;700&family=Roboto:ital,wght@0,400;0,500;0,700;1,400&display=swap" rel="stylesheet">
<style>
:root{
  --orange:#f7931e;
  --orange-dark:#ee7f0f;
  --ink:#222222;
  --text:#333333;
  --muted:#8a8a8a;
  --panel:#efefef;
  --line:#dcdcdc;
  --white:#ffffff;
}
*{box-sizing:border-box;margin:0;padding:0}
html,body{width:1200px;height:4425px;overflow:hidden}
body{position:relative;background:var(--white);font-family:"Roboto",sans-serif;color:var(--text)}
.abs{position:absolute}
h1,h2,h3,.display{font-family:"Rubik",sans-serif}
.accent{color:var(--orange)}
.btn{display:inline-flex;align-items:center;justify-content:center;background:var(--orange);color:var(--white);border-radius:30px;font-size:13px;font-weight:500;text-decoration:none}

/* header */
.site-header{left:0;top:0;width:1200px;height:112px;border-top:4px solid var(--orange);background:var(--white)}
.brand{left:112px;top:28px;display:flex;align-items:center;gap:10px;font-family:"Rubik",sans-serif;font-weight:700;font-size:40px;color:var(--orange)}
.brand-dot{width:14px;height:14px;border-radius:50%;background:var(--ink)}
.main-nav{left:423px;top:48px;display:flex;gap:33px;font-size:13.5px;color:var(--ink)}
.main-nav a{color:inherit;text-decoration:none;position:relative}
.main-nav a.current{color:var(--orange)}
.main-nav a.current::after{content:"";position:absolute;left:0;right:0;bottom:-10px;height:2px;background:var(--orange)}
.login{left:1030px;top:48px;font-size:13.5px;color:var(--ink);display:flex;align-items:center;gap:6px}

/* hero */
.hero{left:0;top:112px;width:1200px;height:565px;background:linear-gradient(90deg,#e9e9e9 0%,#d8d8d8 30%,#3a3a3a 34%,#2b2b2b 66%,#d4d4d4 70%,#ececec 100%)}
.hero-title{left:0;width:1200px;top:130px;text-align:center;font-family:"Rubik",sans-serif;font-weight:700;font-size:76px;color:var(--white)}
.hero-title span{color:var(--orange)}
.hero-cta{left:625px;top:233px;width:150px;height:42px}

/* services */
.services{left:112px;top:713px;width:976px;height:130px;display:flex}
.service{flex:1;display:flex;flex-direction:column;align-items:center;border-right:1px solid var(--line);padding-top:8px;font-size:13.5px;color:var(--ink);text-align:center;line-height:26px}
.service:last-child{border-right:none}
.service svg{width:44px;height:44px;margin-bottom:8px}

/* about */
.about-photo{left:112px;top:941px;width:488px;height:497px;background:linear-gradient(135deg,#f1efe9,#d9d3c8 55%,#b8824a);box-shadow:0 8px 24px rgba(0,0,0,.18);z-index:2}
.about-panel{left:600px;top:993px;width:488px;height:395px;background:var(--panel)}
.about-copy{left:657px;top:1045px;width:372px}
.section-title{font-family:"Rubik",sans-serif;font-weight:700;font-size:32px;color:var(--ink);text-transform:uppercase}
.body-copy{font-size:13px;line-height:26px;color:var(--muted);text-align:justify}
.about-copy .body-copy{margin-top:10px}
.about-copy .btn{margin-top:22px;width:142px;height:46px}

/* targets */
.targets{left:0;top:1543px;width:1200px;height:548px;background:linear-gradient(180deg,#ededed,#e9e9e9 70%,#f1f1f1)}
.centered-title{left:0;width:1200px;text-align:center}
.target{top:1713px;width:309px;height:278px}
.target-photo{position:absolute;left:0;top:0;width:100%;height:100%;background:linear-gradient(135deg,#e2e2e2,#9a9a9a)}
.target-caption{position:absolute;left:24px;top:142px;width:262px;height:134px;background:var(--white);text-align:center;padding-top:30px;box-shadow:0 4px 12px rgba(0,0,0,.06)}
.target-caption h3{font-size:17px;font-weight:500;color:var(--ink)}
.target-caption p{font-size:13px;line-height:26px;color:var(--muted);margin-top:6px}

/* technicians */
.tech-title{left:112px;top:2185px;font-size:34px;line-height:44px}
.review{top:2304px;width:314px;height:206px;background:var(--white);box-shadow:0 2px 12px rgba(0,0,0,.12);padding:22px 24px}
.review-head{display:flex;gap:14px;align-items:center}
.avatar{width:62px;height:62px;border-radius:50%;background:linear-gradient(160deg,#c9d9ea,#8ea8c2)}
.review-name{font-family:"Rubik",sans-serif;font-size:14px;color:var(--muted)}
.review-role{font-size:12px;color:var(--muted);margin-top:6px}
.review-quote{font-style:italic;font-size:12px;line-height:21px;color:var(--muted);text-align:justify;margin-top:10px}
.review-foot{display:flex;justify-content:space-between;margin-top:12px;font-size:12px;color:var(--text)}
.stars{color:var(--orange);letter-spacing:2px}

/* blog */
.blog{left:0;top:2613px;width:1200px;height:642px;background:var(--orange)}
.blog-title{top:2708px;color:var(--white);font-size:36px}
.post{top:2803px;width:287px;height:358px;background:var(--white);border-radius:6px;overflow:hidden}
.post.faded{opacity:.35}
.post-photo{height:185px;background:linear-gradient(135deg,#d9d9d9,#7d7d7d)}
.post-body{padding:18px 25px}
.post-date{font-size:12px;color:var(--muted)}
.post-title{font-family:"Roboto",sans-serif;font-size:17px;font-weight:500;line-height:26px;color:var(--ink);margin-top:8px}
.post-excerpt{font-size:13px;line-height:24px;color:var(--muted);margin-top:6px}

/* featured */
.featured-title{top:3350px}
.partner{top:3430px;width:180px;height:100px;background:var(--white);box-shadow:0 2px 12px rgba(0,0,0,.1);display:flex;align-items:center;justify-content:center}
.badge{background:#d8d8d8;opacity:.8}

/* ready */
.ready-panel{left:112px;top:3631px;width:488px;height:397px;background:var(--panel)}
.ready-copy{left:174px;top:3695px;width:372px}
.ready-copy h2{font-size:34px;line-height:42px;color:var(--ink)}
.ready-copy .body-copy{margin-top:22px}
.ready-copy .btn{margin-top:32px;width:142px;height:48px}
.ready-photo{left:600px;top:3631px;width:488px;height:397px;background:linear-gradient(90deg,#e4e4e4,#f6f6f6 45%,#cfcfcf 70%,#ececec)}

/* footer */
.footer-col{top:4125px}
.footer-col h4{font-family:"Rubik",sans-serif;font-size:19px;font-weight:500;color:var(--ink);margin-bottom:14px}
.footer-col a{display:block;font-size:12.5px;line-height:26px;color:var(--muted);text-decoration:none}
.newsletter{left:776px;top:4168px;width:314px;height:34px;border-bottom:1px solid #c8c8c8;display:flex;justify-content:space-between;align-items:center;font-size:12.5px;color:var(--text);padding:0 8px}
.follow{left:776px;top:4236px;display:flex;align-items:center;gap:10px;font-size:12.5px;color:var(--muted)}
.social{width:28px;height:28px;border-radius:50%}
.contact-mail{left:776px;top:4294px;font-size:12.5px;color:var(--muted)}
.footer-rule{left:112px;top:4351px;width:976px;height:1px;background:#9a9a9a}
.copyright{left:0;width:1200px;top:4377px;text-align:center;font-size:12.5px;color:var(--muted)}
</style>
</head>
<body>

<header class="abs site-header">
  <div class="abs brand"><span class="brand-dot"></span>Brava Nest</div>
  <nav class="abs main-nav">
    <a class="current" href="#">Home</a>
    <a href="#">About Us</a>
    <a href="#">Areas Served</a>
    <a href="#">Pricing and Services</a>
    <a href="#">Contact Us</a>
  </nav>
  <div class="abs login">
    <svg width="15" height="15" viewBox="0 0 16 16" fill="none" stroke="#222" stroke-width="1.4"><circle cx="8" cy="8" r="7"/><circle cx="8" cy="6.3" r="2.4"/><path d="M3.5 13c1-2 2.6-3 4.5-3s3.5 1 4.5 3"/></svg>
    Login
  </div>
</header>

<section class="abs hero" role="img" aria-label="Two technicians in grey overalls mounting a large flat-screen TV between two speakers">
  <h1 class="abs hero-title"><span>Brava</span> Nest</h1>
  <a class="abs btn hero-cta" href="#">GET STARTED</a>
</section>

<section class="abs services">
  <div class="service">
    <svg viewBox="0 0 44 44" fill="none" stroke="#444" stroke-width="1.6"><rect x="13" y="4" width="18" height="34" rx="3"/><line x1="19" y1="33" x2="25" y2="33"/><rect x="6" y="14" width="12" height="14" rx="2"/><path d="M30 18h8M30 24h8"/></svg>
    Phone Repair
  </div>
  <div class="service">
    <svg viewBox="0 0 44 44" fill="none" stroke="#444" stroke-width="1.6"><rect x="5" y="6" width="28" height="20" rx="2"/><path d="M14 32h10M19 26v6"/><rect x="31" y="18" width="9" height="18" rx="2"/><path d="M10 20l6-8M16 20l6-8"/></svg>
    TV Mounting
  </div>
  <div class="service">
    <svg viewBox="0 0 44 44" fill="none" stroke="#444" stroke-width="1.6"><path d="M10 10l26 8-4 8-26-8z"/><path d="M18 22l-2 8H6M6 24v12"/><circle cx="30" cy="20" r="2"/></svg>
    Security Camera<br>Installation
  </div>
  <div class="service">
    <svg viewBox="0 0 44 44" fill="none" stroke="#444" stroke-width="1.6"><rect x="5" y="14" width="34" height="8" rx="2"/><rect x="5" y="26" width="34" height="8" rx="2"/><circle cx="10" cy="18" r="1"/><circle cx="10" cy="30" r="1"/><path d="M30 8a6 6 0 0 1 8 0M32 11a3 3 0 0 1 4 0"/></svg>
    Networking / Wi-Fi
  </div>
  <div class="service">
    <svg viewBox="0 0 44 44" fill="none" stroke="#444" stroke-width="1.6"><path d="M6 22L22 8l16 14"/><path d="M10 19v17h24V19"/><rect x="18" y="26" width="8" height="10"/><path d="M19 16a4 4 0 0 1 6 0"/></svg>
    Smart Home<br>Services
  </div>
  <div class="service">
    <svg viewBox="0 0 44 44" fill="none" stroke="#444" stroke-width="1.6"><rect x="6" y="6" width="32" height="24" rx="3"/><path d="M14 30l-4 8 10-8"/><path d="M15 12l14 12M29 12L15 24"/></svg>
    IT Support
  </div>
</section>

<div class="abs about-photo" role="img" aria-label="Woman in an orange shirt using a smart home control tablet in a bright living room"></div>
<div class="abs about-panel"></div>
<div class="abs about-copy">
  <h2 class="section-title">About <span class="accent">Bravanest</span></h2>
  <p class="body-copy">Lorem ipsum dolor sit amet, consectetur adipiscing elit, sed do eiusmod tempor incididunt ut labore et dolore magna aliqua. Ut enim ad minim veniam, quis nostrud exercitation ullamco laboris nisi ut aliquip ex ea commodo Lorem ipsum dolor sit amet, consectetur adipiscing elit, sed do eiusmod tempor incididunt ut labore et dolore magna aliqua.</p>
  <a class="btn" href="#">Learn more &#10140;</a>
</div>

<section class="abs targets" role="img" aria-label="Faint background of a ceiling security camera"></section>
<h2 class="abs section-title centered-title" style="top:1638px">Our <span class="accent">Targets</span> Are</h2>
<article class="abs target" style="left:112px">
  <div class="target-photo" role="img" aria-label="Smiling woman holding a tablet beside a wall-mounted control panel"></div>
  <div class="target-caption"><h3>Smart Home</h3><p>Lorem ipsum dolor sit amet,<br>consectetur adipiscin</p></div>
</article>
<article class="abs target" style="left:446px">
  <div class="target-photo" role="img" aria-label="Technician in blue workwear installing a TV in a white living room"></div>
  <div class="target-caption"><h3>Installation</h3><p>Lorem ipsum dolor sit amet,<br>consectetur adipiscin</p></div>
</article>
<article class="abs target" style="left:779px">
  <div class="target-photo" role="img" aria-label="Hand using a power drill to repair the back of a TV"></div>
  <div class="target-caption"><h3>Repair Industry</h3><p>Lorem ipsum dolor sit amet,<br>consectetur adipiscin</p></div>
</article>

<h2 class="abs section-title tech-title">Our top technicians are in your<br>neighborhood and beyond</h2>
<article class="abs review" style="left:112px">
  <div class="review-head"><div class="avatar" role="img" aria-label="Technician portrait"></div><div><div class="review-name">Roshan</div><div class="review-role">Trovely technician</div></div></div>
  <p class="review-quote">“Lorem ipsum dolor sit amet, consectetur adipiscing elit, sed do eiusmod tempor incididunt ut labore et dolorealiqua”</p>
  <div class="review-foot"><span>John Doe | Los</span><span class="stars">★★★★★</span></div>
</article>
<article class="abs review" style="left:443px">
  <div class="review-head"><div class="avatar" role="img" aria-label="Technician portrait"></div><div><div class="review-name">Roshan</div><div class="review-role">Trovely technician</div></div></div>
  <p class="review-quote">“Lorem ipsum dolor sit amet, consectetur adipiscing elit, sed do eiusmod tempor incididunt ut labore et dolorealiqua”</p>
  <div class="review-foot"><span>John Doe | Los</span><span class="stars">★★★★★</span></div>
</article>
<article class="abs review" style="left:774px">
  <div class="review-head"><div class="avatar" role="img" aria-label="Technician portrait"></div><div><div class="review-name">Roshan</div><div class="review-role">Trovely technician</div></div></div>
  <p class="review-quote">“Lorem ipsum dolor sit amet, consectetur adipiscing elit, sed do eiusmod tempor incididunt ut labore et dolorealiqua”</p>
  <div class="review-foot"><span>John Doe | Los</span><span class="stars">★★★★★</span></div>
</article>

<section class="abs blog"></section>
<h2 class="abs section-title centered-title blog-title" style="color:#fff">Our Latest Blog</h2>
<article class="abs post faded" style="left:-180px">
  <div class="post-photo" role="img" aria-label="Circuit board close-up"></div>
  <div class="post-body"><div class="post-date">JAN 20, 2020</div><h3 class="post-title">LOREM IPSUM DOLOR SIT AMET, CONSECTETUR</h3><p class="post-excerpt">Lorem ipsum dolor sit amet, conse cte tur adipiscing elit, sed do</p></div>
</article>
<article class="abs post" style="left:137px">
  <div class="post-photo" role="img" aria-label="Technician fitting a ceiling security camera"></div>
  <div class="post-body"><div class="post-date">JAN 20, 2020</div><h3 class="post-title">LOREM IPSUM DOLOR SIT AMET, CONSECTETUR</h3><p class="post-excerpt">Lorem ipsum dolor sit amet, conse cte tur adipiscing elit, sed do</p></div>
</article>
<article class="abs post" style="left:457px">
  <div class="post-photo" role="img" aria-label="Gloved hands repairing an open smartphone"></div>
  <div class="post-body"><div class="post-date">JAN 20, 2020</div><h3 class="post-title">LOREM IPSUM DOLOR SIT AMET, CONSECTETUR</h3><p class="post-excerpt">Lorem ipsum dolor sit amet, conse cte tur adipiscing elit, sed do</p></div>
</article>
<article class="abs post" style="left:775px">
  <div class="post-photo" role="img" aria-label="Two technicians mounting a TV on a wall"></div>
  <div class="post-body"><div class="post-date">JAN 20, 2020</div><h3 class="post-title">LOREM IPSUM DOLOR SIT AMET, CONSECTETUR</h3><p class="post-excerpt">Lorem ipsum dolor sit amet, conse cte tur adipiscing elit, sed do</p></div>
</article>
<article class="abs post faded" style="left:1094px">
  <div class="post-photo" role="img" aria-label="Laptop repair close-up"></div>
  <div class="post-body"><div class="post-date">JAN 20, 2020</div><h3 class="post-title">LOREM IPSUM DOLOR SIT AMET, CONSECTETUR</h3><p class="post-excerpt">Lorem ipsum dolor sit amet, conse cte tur adipiscing elit, sed do</p></div>
</article>

<h2 class="abs section-title centered-title featured-title">Featured In</h2>
<div class="abs partner" style="left:112px"><div class="badge" style="width:80px;height:40px"></div></div>
<div class="abs partner" style="left:311px"><div class="badge" style="width:44px;height:44px;border-radius:50%"></div></div>
<div class="abs partner" style="left:510px"><div class="badge" style="width:50px;height:50px;border-radius:50%;background:#9c9c9c"></div></div>
<div class="abs partner" style="left:709px"><div class="badge" style="width:90px;height:34px"></div></div>
<div class="abs partner" style="left:908px"><div class="badge" style="width:110px;height:30px;border-radius:15px"></div></div>

<div class="abs ready-panel"></div>
<div class="abs ready-copy">
  <h2>READY TO<br><span class="accent">GET STARTED?</span></h2>
  <p class="body-copy">Lorem ipsum dolor sit amet, consectetur adipiscing elit, sed do eiusmod tempor incididunt ut labore et dolore magna aliqua. Ut enim ad minim veniam, quis nostrud exercitation ullamco laboris nisi ut aliquip</p>
  <a class="btn" href="#">Book a Service</a>
</div>
<div class="abs ready-photo" role="img" aria-label="Smiling technician giving a thumbs up beside a colleague installing a wall charger"></div>

<div class="abs footer-col" style="left:112px"><h4>Company</h4><a>Home</a><a>How It Works</a><a>Become a Tech</a><a>Pricing</a><a>Careers</a><a>Blog</a></div>
<div class="abs footer-col" style="left:280px"><h4>Resources</h4><a>TV mounting</a><a>Garage Doors</a><a>Appliances</a><a>Refrigerators</a><a>Dishwashers</a><a>Ovens &amp; Stoves</a></div>
<div class="abs footer-col" style="left:447px"><h4>Partnership</h4><a>Telvora</a><a>SafeGrid</a><a>Hivue</a><a>Trovely for business</a></div>
<div class="abs footer-col" style="left:616px"><h4>Legal</h4><a>Privacy policy</a><a>Terms</a><a>Trovely+ Terms</a><a>Guarantee</a></div>
<div class="abs footer-col" style="left:771px"><h4>Stay Connected</h4></div>
<div class="abs newsletter"><span>Email address</span>
  <svg width="14" height="14" viewBox="0 0 16 16" fill="#f7931e"><path d="M1 8l14-7-4 14-3-5z"/></svg>
</div>
<div class="abs follow">Follow us :
  <span class="social" style="background:#4267b2"></span>
  <span class="social" style="background:#55acee"></span>
  <span class="social" style="background:#0e76a8"></span>
  <span class="social" style="background:#cb2027"></span>
</div>
<div class="abs contact-mail">info@bravanest.example</div>
<div class="abs footer-rule"></div>
<div class="abs copyright">© Copyrights 2020 &nbsp;Brava Nest | All Right Reserved</div>

</body>
</html>
```